Brochure for Flooring

Brochure for bamboo flooring company.

Size can be any size, we aren't married to specific dimension / type.

Files for logo, text, and some photos to get started attached. Designer can also use placeholder photos that we can switch out later.

Themes are Eco Friendly, natural, bamboo...

Thanks, and look forward to seeing your design.

Industry/Entity Type

Flooring

```html
<!DOCTYPE html>
<html lang="en">
<head>
<meta charset="UTF-8">
<title>Bambusa Brochure Cover</title>
<link href="https://fonts.googleapis.com/css2?family=Open+Sans:wght@400;700&display=swap" rel="stylesheet">
<style>
  :root {
    --backdrop: #4b4e4b;
    --leaf-green: #8cc63f;
    --band-brown: #6b4e33;
    --text-light: #ffffff;
    --wall-light: #f3ead2;
    --wall-warm: #e2d2a8;
    --cabinet: #6e5232;
    --wood-glow: #efb86a;
    --wood-light: #dc9a4c;
    --wood-mid: #c07630;
    --wood-deep: #8e5020;
  }
  html, body {
    margin: 0;
    padding: 0;
    width: 1200px;
    height: 896px;
    overflow: hidden;
    background: var(--backdrop);
    font-family: "Open Sans", Arial, sans-serif;
  }
  .canvas {
    position: relative;
    width: 1200px;
    height: 896px;
  }
  .brochure-cover {
    position: absolute;
    left: 244px;
    top: 48px;
    width: 712px;
    height: 800px;
    overflow: hidden;
    box-shadow: 0 6px 24px rgba(0, 0, 0, 0.35);
  }
  .cover-photo {
    position: absolute;
    inset: 0 0 70px 0;
    background:
      radial-gradient(ellipse 40% 22% at 70% 12%, rgba(255, 252, 240, 0.9), rgba(255, 252, 240, 0) 100%),
      radial-gradient(ellipse 30% 14% at 18% 30%, rgba(70, 50, 30, 0.55), rgba(70, 50, 30, 0) 100%),
      radial-gradient(ellipse 45% 10% at 55% 58%, rgba(255, 220, 150, 0.55), rgba(255, 220, 150, 0) 100%),
      radial-gradient(ellipse 35% 8% at 30% 70%, rgba(255, 215, 140, 0.4), rgba(255, 215, 140, 0) 100%),
      linear-gradient(180deg,
        var(--wall-light) 0%,
        var(--wall-warm) 20%,
        #cdb88e 30%,
        var(--cabinet) 40%,
        #a7763f 46%,
        var(--wood-glow) 54%,
        var(--wood-light) 66%,
        var(--wood-mid) 82%,
        var(--wood-deep) 100%);
  }
  .brand-tile {
    position: absolute;
    left: 248px;
    top: 0;
    width: 210px;
    height: 190px;
    background: var(--leaf-green);
    color: var(--text-light);
    display: flex;
    flex-direction: column;
    align-items: center;
    justify-content: flex-end;
    padding-bottom: 26px;
    box-sizing: border-box;
  }
  .brand-mark {
    width: 24px;
    height: 24px;
    border-radius: 50%;
    background: var(--text-light);
    margin-bottom: 26px;
  }
  .brand-name {
    font-size: 36px;
    font-weight: 400;
    letter-spacing: 4px;
    line-height: 1;
    margin: 0;
  }
  .brand-tagline {
    font-size: 10px;
    font-weight: 700;
    margin: 10px 0 0;
    letter-spacing: 0.2px;
  }
  .footer-band {
    position: absolute;
    left: 0;
    bottom: 0;
    width: 100%;
    height: 70px;
    background: var(--band-brown);
    display: flex;
    align-items: center;
    justify-content: center;
  }
  .web-address {
    color: var(--text-light);
    font-size: 15px;
    font-weight: 700;
    letter-spacing: 0.4px;
  }
</style>
</head>
<body>
  <main class="canvas">
    <article class="brochure-cover">
      <div class="cover-photo" role="img" aria-label="Photo of a bright open-plan kitchen with a glossy bamboo floor, bar stools, a breakfast counter and a dining table by a window"></div>
      <header class="brand-tile">
        <span class="brand-mark" aria-hidden="true"></span>
        <h1 class="brand-name">Bambusa</h1>
        <p class="brand-tagline">natural floors for green homes</p>
      </header>
      <footer class="footer-band">
        <span class="web-address">www.bambusaliving.com</span>
      </footer>
    </article>
  </main>
</body>
</html>
```